SPÄTER FREI!
Zielgruppe
Mein Ebook 'SPÄTER FREI!' soll den Untertitel 'Wie du Schwermut, Abhängigkeit und Alleinsein hinter dir lässt und neu anfängst' haben. Genau darum geht es und das soll das auch Cover vermitteln. Der Autor des Buches heißt Olaf Brenner.

```html
<!DOCTYPE html>
<html lang="de">
<head>
<meta charset="utf-8">
<title>Später Frei – Olaf Brenner</title>
<link rel="stylesheet" href="https://fonts.googleapis.com/css2?family=Fredoka:wght@500;600;700&display=swap">
<style>
  :root {
    --ink-blue: #0a74c4;
    --paper: #ffffff;
    --splash-pink: #d93a8c;
    --splash-orange: #ef8a2c;
    --splash-yellow: #f4c43a;
    --splash-green: #9cc34a;
    --splash-blue: #2a8fd6;
  }
  html, body {
    margin: 0;
    padding: 0;
    width: 848px;
    height: 1200px;
    overflow: hidden;
    background: var(--paper);
  }
  .cover {
    position: relative;
    width: 848px;
    height: 1200px;
    background: var(--paper);
    font-family: "Fredoka", sans-serif;
    color: var(--ink-blue);
    text-align: center;
  }
  .cover-art {
    position: absolute;
    left: 102px;
    top: 372px;
    width: 682px;
    height: 770px;
  }
  .title {
    position: absolute;
    left: 0;
    right: 0;
    top: 56px;
    margin: 0;
    font-weight: 700;
    font-size: 104px;
    line-height: 104px;
    letter-spacing: 3px;
    z-index: 1;
  }
  .title-line { display: block; }
  .title-line.second { padding-left: 24px; }
  .subtitle {
    position: absolute;
    left: 0;
    right: 0;
    top: 280px;
    margin: 0;
    font-weight: 600;
    font-size: 24px;
    line-height: 40px;
    letter-spacing: 1px;
    z-index: 1;
  }
  .subtitle span { display: block; }
  .author {
    position: absolute;
    left: 0;
    right: 0;
    top: 1128px;
    margin: 0;
    font-weight: 600;
    font-size: 29px;
    letter-spacing: 1.5px;
    z-index: 1;
  }
</style>
</head>
<body>
  <main class="cover">
    <h1 class="title">
      <span class="title-line">Später</span>
      <span class="title-line second">Frei</span>
    </h1>
    <p class="subtitle">
      <span>Wie du Schwermut, Abhängigkeit und Alleinsein</span>
      <span>hinter dir lässt und neu anfängst</span>
    </p>

    <svg class="cover-art" viewBox="0 0 682 770" role="img"
         aria-label="Illustration: springende Figur als Silhouette aus bunten Farbspritzern in Pink, Orange, Gelb, Grün und Blau">
      <defs>
        <radialGradient id="splashGlow" cx="52%" cy="45%" r="60%">
          <stop offset="0%" stop-color="var(--splash-yellow)" stop-opacity="0.55"/>
          <stop offset="30%" stop-color="var(--splash-orange)" stop-opacity="0.45"/>
          <stop offset="55%" stop-color="var(--splash-pink)" stop-opacity="0.35"/>
          <stop offset="78%" stop-color="var(--splash-blue)" stop-opacity="0.18"/>
          <stop offset="100%" stop-color="var(--splash-green)" stop-opacity="0"/>
        </radialGradient>
      </defs>
      <rect x="0" y="0" width="682" height="770" rx="60" fill="url(#splashGlow)"/>
    </svg>

    <p class="author">Olaf Brenner</p>
  </main>
</body>
</html>
```